Real Estate Business Folders, Business Cards, Envelopes & Letterhead

Im looking for trendy, modern & professional design concepts for my business folder that will be used for real estate documents and property report presentations. I'm also looking for Business card designs, envelopes and letterhead with a similar theme. I have a logo already and I would like the logo colors to be incorporated in the design concepts.

Target Market(s)

Real Estate Investors, Banks, Financial Institutions

Industry/Entity Type

Real Estate

Colors
0455a3
959595
d3d3d3
848484

Requirements
Must have
• Trendy Modern, High Class look. Please include logo and colors and incorporate some silver or metallic.
• Business Address: 4812 Corvelle Blvd ste 210-300
• Brookhaven, NV 89950
• Phone: 702-555-0147
• Fax : 702-555-0183
• Email: info@mesacrestlandgroup.example
• Website: MesaCrestLandGroup.example

```html
<!DOCTYPE html>
<html lang="en">
<head>
<meta charset="utf-8">
<title>Mesa Crest Land Group — Stationery Set</title>
<link href="https://fonts.googleapis.com/css2?family=Lato:wght@400;700&family=Great+Vibes&display=swap" rel="stylesheet">
<style>
  :root{
    --backdrop:#d3d3d5;
    --paper:#ffffff;
    --paper-soft:#f3f3f3;
    --slate:#848484;
    --silver:#959595;
    --brand-blue:#0455a3;
    --ink:#3a3a3a;
    --ink-soft:#777;
  }
  *{box-sizing:border-box;margin:0;padding:0}
  html,body{width:1200px;height:1200px;overflow:hidden}
  body{background:var(--backdrop);font-family:"Lato",sans-serif;color:var(--ink);position:relative}
  .piece{position:absolute}

  /* Brand name block */
  .brand{display:flex;align-items:center;gap:5px;white-space:nowrap}
  .brand-mark{width:8px;height:8px;background:var(--brand-blue);flex:none}
  .brand-name{font-family:"Lato",sans-serif;font-weight:700;color:var(--brand-blue);letter-spacing:.04em;text-transform:uppercase}
  .brand--light .brand-mark{background:#fff}
  .brand--light .brand-name{color:#fff}

  /* Contact list */
  .contacts{list-style:none;color:var(--ink-soft)}
  .contacts li{display:flex;align-items:center;gap:4px;white-space:nowrap}
  .contacts svg{fill:var(--brand-blue);flex:none}
  .contacts--right li{justify-content:flex-end}

  /* Folder */
  .folder-pocket{left:140px;top:71px;width:366px;height:491px}
  .folder-cover{left:506px;top:71px;width:305px;height:420px;background:var(--slate);display:flex;align-items:center;justify-content:center;padding-bottom:130px}
  .folder-cover .brand-name{font-size:11px}
  .folder-cover .brand-mark{width:9px;height:9px}
  .folder-contacts{left:232px;top:441px;font-size:3.6px;line-height:4.4px}
  .folder-contacts svg{width:3px;height:3px}

  /* Letterhead */
  .letterhead{left:115px;top:613px;width:365px;height:515px;background:var(--paper)}
  .letterhead .brand{position:absolute;left:25px;top:62px}
  .letterhead .brand-name{font-size:8px}
  .letterhead .contacts{position:absolute;left:255px;top:52px;font-size:5px;line-height:6.5px}
  .letterhead .contacts svg{width:4px;height:4px}
  .letter-body{position:absolute;left:24px;top:136px;width:330px;font-size:5.6px;line-height:7px;color:var(--ink-soft)}
  .letter-body .salutation{font-size:7px;color:var(--ink);margin-bottom:14px}
  .letter-body p{margin-bottom:6px;text-align:justify}
  .letter-body p.strong{color:var(--ink);font-weight:700}
  .signature{font-family:"Great Vibes",cursive;font-size:26px;color:#3b3f8a;margin-top:12px;line-height:30px}
  .signer{font-size:7px;color:var(--ink);margin-top:4px}
  .signer-role{font-size:5px;color:var(--ink-soft)}

  /* Business card */
  .card-front{left:466px;top:832px;width:205px;height:117px;background:var(--slate);display:flex;align-items:center;justify-content:center}
  .card-front .brand-name{font-size:7px}
  .card-front .brand-mark{width:6px;height:6px}
  .card-back{left:466px;top:962px;width:205px;height:114px;background:var(--paper)}
  .card-name{position:absolute;left:21px;top:29px;font-size:7.5px;color:var(--ink)}
  .card-role{position:absolute;left:21px;top:39px;font-size:4.5px;color:var(--brand-blue)}
  .card-back .contacts{position:absolute;left:21px;top:50px;font-size:4.3px;line-height:7.2px}
  .card-back .contacts svg{width:3.6px;height:3.6px}

  /* Envelope */
  .envelope-back{left:590px;top:544px;width:443px;height:221px;background:var(--paper-soft)}
  .envelope-flap{position:absolute;left:0;top:0;width:443px;height:73px}
  .envelope-front{left:703px;top:666px;width:444px;height:222px;background:var(--paper-soft)}
  .envelope-front .brand{position:absolute;right:28px;top:58px}
  .envelope-front .brand-name{font-size:10.5px}
  .envelope-front .contacts{position:absolute;right:28px;top:123px;font-size:8px;line-height:11.8px}
  .envelope-front .contacts svg{width:6px;height:6px}
  .envelope-window{position:absolute;left:33px;top:118px;width:156px;height:70px;border-radius:14px;background:var(--slate)}
</style>
</head>
<body>

<!-- Folder: inside pocket -->
<svg class="piece folder-pocket" viewBox="0 0 366 491" aria-hidden="true">
  <polygon fill="#ffffff" points="60,0 366,0 366,420 316,491 60,491 60,440 0,380 0,33"/>
</svg>
<ul class="piece contacts folder-contacts">
  <li><svg viewBox="0 0 10 10"><rect width="10" height="10"/></svg>702-555-0147</li>
  <li><svg viewBox="0 0 10 10"><rect width="10" height="10"/></svg>702-555-0183</li>
  <li><svg viewBox="0 0 10 10"><rect width="10" height="10"/></svg>info@mesacrestlandgroup.example</li>
  <li><svg viewBox="0 0 10 10"><rect width="10" height="10"/></svg>MesaCrestLandGroup.example</li>
  <li><svg viewBox="0 0 10 10"><rect width="10" height="10"/></svg>4812 Corvelle Blvd ste 210-300</li>
  <li>&nbsp;&nbsp;- Brookhaven, NV 89950</li>
</ul>

<!-- Folder: cover -->
<section class="piece folder-cover">
  <div class="brand brand--light"><span class="brand-mark"></span><span class="brand-name">Mesa Crest Land Group</span></div>
</section>

<!-- Letterhead -->
<section class="piece letterhead">
  <div class="brand"><span class="brand-mark"></span><span class="brand-name">Mesa Crest Land Group</span></div>
  <ul class="contacts">
    <li><svg viewBox="0 0 10 10"><path d="M2 0h2l1 3-1.5 1a6 6 0 0 0 2.5 2.5L7 5l3 1v2c0 1-1 2-2 2C4 10 0 6 0 2 0 1 1 0 2 0z"/></svg>702-555-0147</li>
    <li><svg viewBox="0 0 10 10"><rect x="1" y="3" width="8" height="6"/><rect x="3" y="0" width="4" height="3"/></svg>702-555-0183</li>
    <li><svg viewBox="0 0 10 10"><rect y="2" width="10" height="6"/></svg>info@mesacrestlandgroup.example</li>
    <li><svg viewBox="0 0 10 10"><circle cx="5" cy="5" r="5"/></svg>MesaCrestLandGroup.example</li>
    <li><svg viewBox="0 0 10 10"><path d="M5 0a4 4 0 0 1 4 4c0 3-4 6-4 6S1 7 1 4a4 4 0 0 1 4-4z"/></svg>4812 Corvelle Blvd ste 210-300</li>
    <li>&nbsp;&nbsp;- Brookhaven, NV 89950</li>
  </ul>
  <div class="letter-body">
    <p class="salutation">Dear, Mr_________</p>
    <p>Lorem Ipsum is simply dummy text of the printing and typesetting industry. Lorem Ipsum has been the industry's standard dummy text ever since the 1500s, when an unknown printer took a galley of type and scrambled it to make a type specimen book. It has survived not only five centuries, but also the leap into electronic typesetting, remaining essentially unchanged.</p>
    <p class="strong">Lorem Ipsum is simply dummy text of the printing and typesetting industry. Lorem Ipsum has been the industry's standard dummy text ever since the 1500s, when an unknown printer took a galley of type and scrambled it to make a type specimen book.</p>
    <p>Lorem Ipsum is simply dummy text of the printing and typesetting industry. Lorem Ipsum has been the industry's standard dummy text ever since the 1500s, when an unknown printer took a galley of type and scrambled it to make a type specimen book.</p>
    <p>Lorem Ipsum is simply dummy text of the printing and typesetting industry.</p>
    <div class="signature">Signature</div>
    <div class="signer">Your Name</div>
    <div class="signer-role">Designation</div>
  </div>
</section>

<!-- Envelope: back -->
<section class="piece envelope-back">
  <svg class="envelope-flap" viewBox="0 0 443 73" aria-hidden="true">
    <path fill="#848484" d="M0 0h443l-8 62q-2 11-14 11H24q-12 0-14-11z"/>
  </svg>
</section>

<!-- Envelope: front -->
<section class="piece envelope-front">
  <div class="brand"><span class="brand-mark"></span><span class="brand-name">Mesa Crest Land Group</span></div>
  <div class="envelope-window"></div>
  <ul class="contacts contacts--right">
    <li>702-555-0147<svg viewBox="0 0 10 10"><path d="M2 0h2l1 3-1.5 1a6 6 0 0 0 2.5 2.5L7 5l3 1v2c0 1-1 2-2 2C4 10 0 6 0 2 0 1 1 0 2 0z"/></svg></li>
    <li>702-555-0183<svg viewBox="0 0 10 10"><rect x="1" y="3" width="8" height="6"/><rect x="3" y="0" width="4" height="3"/></svg></li>
    <li>info@mesacrestlandgroup.example<svg viewBox="0 0 10 10"><rect y="2" width="10" height="6"/></svg></li>
    <li>MesaCrestLandGroup.example<svg viewBox="0 0 10 10"><circle cx="5" cy="5" r="5"/></svg></li>
    <li>4812 Corvelle Blvd ste 210-300<svg viewBox="0 0 10 10"><path d="M5 0a4 4 0 0 1 4 4c0 3-4 6-4 6S1 7 1 4a4 4 0 0 1 4-4z"/></svg></li>
    <li>- Brookhaven, NV 89950&nbsp;&nbsp;&nbsp;</li>
  </ul>
</section>

<!-- Business card: front -->
<section class="piece card-front">
  <div class="brand brand--light"><span class="brand-mark"></span><span class="brand-name">Mesa Crest Land Group</span></div>
</section>

<!-- Business card: back -->
<section class="piece card-back">
  <div class="card-name">Dana Whitfield</div>
  <div class="card-role">Director</div>
  <ul class="contacts">
    <li><svg viewBox="0 0 10 10"><path d="M2 0h2l1 3-1.5 1a6 6 0 0 0 2.5 2.5L7 5l3 1v2c0 1-1 2-2 2C4 10 0 6 0 2 0 1 1 0 2 0z"/></svg>702-555-0147</li>
    <li><svg viewBox="0 0 10 10"><rect x="1" y="3" width="8" height="6"/><rect x="3" y="0" width="4" height="3"/></svg>702-555-0183</li>
    <li><svg viewBox="0 0 10 10"><rect y="2" width="10" height="6"/></svg>info@mesacrestlandgroup.example</li>
    <li><svg viewBox="0 0 10 10"><circle cx="5" cy="5" r="5"/></svg>MesaCrestLandGroup.example</li>
    <li><svg viewBox="0 0 10 10"><path d="M5 0a4 4 0 0 1 4 4c0 3-4 6-4 6S1 7 1 4a4 4 0 0 1 4-4z"/></svg>4812 Corvelle Blvd ste 210-300</li>
    <li>&nbsp;&nbsp;- Brookhaven, NV 89950</li>
  </ul>
</section>

</body>
</html>
```